Concrete Construction page for marketing my business

I need a nice website where I can upload photos of current work, at the moment I am using facebook but I would like to have my own webpage, I would need a nice and easy menu at the top of the page

you can find my facebook page here https://www.socialwall.net/StoneVista

For images and ideas...

My Facebook page is

www.socialwall.net/stonevistaadelaide/

```html
<!DOCTYPE html>
<html lang="en">
<head>
<meta charset="utf-8">
<title>StoneVista — Concrete Construction</title>
<link href="https://fonts.googleapis.com/css2?family=Exo+2:wght@500;600;700&family=Mulish:wght@400;600;700;800&display=swap" rel="stylesheet">
<style>
:root{
  --blue:#34509a;
  --blue-dark:#2b4487;
  --ink:#1f2330;
  --text:#3a3d47;
  --muted:#8a8d96;
  --light:#f4f2f3;
  --line:#d7d8de;
  --white:#ffffff;
}
*{box-sizing:border-box;margin:0;padding:0}
html,body{width:1200px;height:4721px;overflow:hidden}
body{font-family:"Mulish",sans-serif;color:var(--text);background:var(--white);position:relative}
.abs{position:absolute}
.heading{font-family:"Exo 2",sans-serif;font-weight:600;text-transform:uppercase;letter-spacing:2px;color:var(--ink);font-size:31px}
.center{text-align:center;left:0;width:1200px}
.rule{position:absolute;height:4px;width:38px;background:var(--blue)}
.btn{position:absolute;background:var(--blue);color:var(--white);font-weight:800;font-size:14px;text-transform:uppercase;display:flex;align-items:center;justify-content:center;letter-spacing:.3px}
.brand{font-family:"Mulish",sans-serif;font-weight:800;font-size:36px;letter-spacing:1px;text-transform:uppercase}

/* header */
.site-header{position:absolute;top:0;left:0;width:1200px;height:132px;background:var(--white)}
.site-header .brand{position:absolute;left:132px;top:40px;color:var(--blue)}
.header-call{position:absolute;left:660px;top:22px;display:flex;gap:14px;align-items:center}
.header-call small{display:block;font-size:14px;color:var(--ink)}
.header-call strong{font-size:18px;color:var(--blue);font-weight:700}
.nav{position:absolute;top:80px;left:466px;display:flex;gap:0}
.nav a{font-size:14px;color:var(--ink);text-decoration:none;padding:6px 10px;margin-right:10px;text-transform:uppercase}
.nav a.active{background:var(--blue);color:var(--white)}

/* hero */
.hero{position:absolute;top:132px;left:0;width:1200px;height:500px;background:linear-gradient(180deg,#2c3440 0%,#3f4652 45%,#5a5f66 100%)}
.hero h1{position:absolute;top:95px;font-family:"Exo 2",sans-serif;font-weight:600;font-size:43px;line-height:52px;color:var(--white);letter-spacing:2px;text-transform:uppercase}
.hero p{position:absolute;top:218px;font-size:20px;color:var(--white);font-weight:600}
.dots{position:absolute;display:flex;gap:10px}
.dots i{width:11px;height:11px;border-radius:50%;background:var(--white);display:block}
.dots i.on{background:var(--blue);border:2px solid var(--white)}

/* about */
.about{position:absolute;top:632px;left:0;width:1200px;height:526px;background:var(--light)}
.photo{position:absolute}
.about p{position:absolute;left:672px;width:388px;font-size:13.5px;line-height:21px;text-align:justify;color:var(--text)}

/* process */
.process{position:absolute;top:1158px;left:0;width:1200px;height:500px;background:var(--white)}
.step{position:absolute;width:200px;text-align:center}
.step .ring{width:160px;height:160px;border-radius:50%;border:1.5px solid var(--blue);background:#f5f6fa;margin:0 auto;position:relative}
.step .ring span{position:absolute;left:44px;top:44px;width:72px;height:72px;border-radius:12px;background:#dfe4f0}
.step .num{position:absolute;top:-28px;left:72px;width:56px;height:56px;border-radius:50%;background:var(--blue);color:var(--white);font-weight:700;font-size:20px;display:flex;align-items:center;justify-content:center}
.step h3{margin-top:26px;font-size:19px;font-weight:600;color:var(--ink)}

/* why choose */
.why{position:absolute;top:1658px;left:0;width:1200px;height:538px;background:var(--light);overflow:hidden}
.feature{position:absolute;width:227px;height:76px;background:var(--white);border:1px solid var(--line);display:flex;align-items:center;gap:16px;padding-left:18px;font-size:15px;line-height:21px;color:var(--ink)}
.feature i{width:34px;height:34px;background:var(--blue);border-radius:4px;flex:none;opacity:.9}
.thumb{position:absolute;border-radius:50%;border:6px solid var(--white)}

/* services */
.services{position:absolute;top:2196px;left:0;width:1200px;height:619px;background:var(--white)}
.card{position:absolute;top:171px;width:224px;height:385px;border:1px solid var(--line);background:var(--white)}
.card .pic{height:201px}
.card h3{margin:28px 0 0 26px;font-size:15.5px;font-weight:700;text-transform:uppercase;color:var(--ink)}
.card p{margin:8px 26px 0 26px;font-size:12px;line-height:16px;color:var(--text)}
.card .more{position:absolute;left:26px;top:327px;width:92px;height:28px;background:var(--blue);color:var(--white);font-size:10.5px;font-weight:800;display:flex;align-items:center;justify-content:center}
.card.active{background:var(--blue);border-color:var(--blue)}
.card.active h3,.card.active p{color:var(--white)}
.card.active .more{background:var(--white);color:var(--blue)}
.arrow{position:absolute;width:36px;height:36px;border-radius:50%;border:1.5px solid var(--blue);display:flex;align-items:center;justify-content:center}

/* testimonials */
.testimonials{position:absolute;top:2815px;left:0;width:1200px;height:485px;background:linear-gradient(180deg,#eceaec,#e4e3e6)}
.quote{position:absolute;left:229px;top:190px;width:742px;font-size:17px;line-height:26px;text-align:center;color:var(--text)}
.qmark{position:absolute;font-family:Georgia,serif;font-size:90px;color:var(--blue);font-weight:700;line-height:1}

/* projects */
.projects{position:absolute;top:3300px;left:0;width:1200px;height:440px;background:var(--white)}
.shot{position:absolute;top:171px;height:224px}

/* quotation */
.quotation{position:absolute;top:3740px;left:0;width:1200px;height:673px;background:linear-gradient(135deg,#3b4150,#5b6070 50%,#3c4250)}
.form-card{position:absolute;left:249px;top:52px;width:702px;height:568px;background:rgba(244,244,247,.95)}
.field{position:absolute;height:41px;border:1px solid #7f8598;background:rgba(255,255,255,.4);font-size:12px;color:var(--text);padding:0 18px;display:flex;align-items:center}

/* footer */
.site-footer{position:absolute;top:4413px;left:0;width:1200px;height:308px;background:var(--blue);color:var(--white)}
.site-footer .brand{position:absolute;left:132px;top:52px;color:var(--white)}
.site-footer h4{position:absolute;top:46px;font-size:15px;font-weight:700;text-transform:uppercase}
.foot-list{position:absolute;top:82px;font-size:11.5px;line-height:18px}
.social{position:absolute;left:886px;top:80px;display:flex;gap:8px}
.social i{width:32px;height:32px;border-radius:50%;border:1.5px solid var(--white);display:block}
</style>
</head>
<body>

<header class="site-header">
  <div class="brand">StoneVista</div>
  <div class="header-call">
    <svg width="32" height="32" viewBox="0 0 24 24" fill="none" stroke="#34509a" stroke-width="1.4"><path d="M5 3h3l2 5-2 1.5a11 11 0 0 0 6 6L15.5 14l5 2v3a2 2 0 0 1-2 2A16 16 0 0 1 3 5a2 2 0 0 1 2-2z"/></svg>
    <div><small>Call Us</small><strong>+61 400 555 123</strong></div>
  </div>
  <div class="btn" style="left:888px;top:22px;width:180px;height:41px;font-size:13px">Free Quotation</div>
  <nav class="nav">
    <a class="active">Home</a><a>Residential</a><a>Commercial</a><a>About Us</a><a>Gallery</a><a>Contact Us</a>
  </nav>
</header>

<section class="hero" role="img" aria-label="Photo of a finished concrete driveway in front of a garden">
  <h1 class="center" style="text-align:center">Solid Solutions in<br>Concrete Construction</h1>
  <p class="center" style="text-align:center">Delivering durable concrete solutions for lasting success.</p>
  <div class="btn" style="left:505px;top:268px;width:190px;height:52px">Free Quotation</div>
  <div class="dots" style="left:560px;top:449px"><i class="on"></i><i></i><i></i><i></i></div>
</section>

<section class="about">
  <div class="photo" role="img" aria-label="Exposed aggregate concrete path" style="left:145px;top:57px;width:414px;height:414px;border-radius:50%;background:radial-gradient(circle at 40% 45%,#b7a994,#8c8070 70%,#6d6a5e)"></div>
  <div class="photo" role="img" aria-label="House with a new concrete driveway" style="left:385px;top:257px;width:220px;height:220px;border-radius:50%;border:8px solid var(--white);background:linear-gradient(180deg,#5f86c4 0%,#e6e6e6 45%,#7b7b7e 100%)"></div>
  <h2 class="heading abs" style="left:672px;top:88px">About Us</h2>
  <div class="rule" style="left:672px;top:143px;width:78px"></div>
  <p style="top:184px">Lorem ipsum dolor sit amet, consectetur adipiscing elit, sed do eiusmod tempor incididunt ut labore et dolore magna aliqua. Ut enim ad minim veniam, quis nostrud exercitation ullamco laboris nisi ut aliquip ex ea commodo consequat. Duis aute irure dolor in reprehea.</p>
  <p style="top:313px">Lorem ipsum dolor sit amet, consectetur adipiscing elit, sed do eiusmod tempor incididunt ut labore et dolore magna tempor incididunt aliqua.</p>
  <div class="btn" style="left:672px;top:408px;width:130px;height:47px;font-size:12px">Learn More</div>
</section>

<section class="process">
  <h2 class="heading abs center" style="top:64px">Our Process</h2>
  <div class="rule" style="left:576px;top:128px;width:48px"></div>
  <div class="step" style="left:114px;top:218px"><div class="ring"><div class="num">01</div><span role="img" aria-label="Excavation icon"></span></div><h3>Lorem ipsum</h3></div>
  <div class="step" style="left:363px;top:218px"><div class="ring"><div class="num">02</div><span role="img" aria-label="Floor grinding icon"></span></div><h3>Lorem ipsum</h3></div>
  <div class="step" style="left:629px;top:218px"><div class="ring"><div class="num">03</div><span role="img" aria-label="Surface finishing icon"></span></div><h3>Lorem ipsum</h3></div>
  <div class="step" style="left:886px;top:218px"><div class="ring"><div class="num">04</div><span role="img" aria-label="Polishing icon"></span></div><h3>Lorem ipsum</h3></div>
</section>

<section class="why">
  <div class="abs" role="img" aria-label="Close-up of exposed aggregate concrete" style="left:640px;top:0;width:560px;height:538px;clip-path:polygon(148px 0,560px 0,560px 538px,0 538px);background:linear-gradient(135deg,#b5a895,#8f8475 60%,#cfcbc5)"></div>
  <div class="thumb" role="img" aria-label="Grey concrete detail" style="left:726px;top:1761px;top:103px;width:88px;height:88px;background:#8a8b8d"></div>
  <div class="thumb" role="img" aria-label="Dark sealed concrete detail" style="left:681px;top:218px;width:88px;height:88px;background:#3f4553"></div>
  <div class="thumb" role="img" aria-label="Concrete edge beside lawn" style="left:648px;top:337px;width:88px;height:88px;background:linear-gradient(135deg,#7c9a4e,#d9d3c3)"></div>
  <h2 class="heading abs" style="left:128px;top:42px">Why Choose Us</h2>
  <div class="rule" style="left:130px;top:100px"></div>
  <div class="feature" style="left:132px;top:137px"><i role="img" aria-label="Onsite icon"></i>Our Finishes Are<br>Created Onsite</div>
  <div class="feature" style="left:363px;top:137px"><i role="img" aria-label="Quality icon"></i>We Use Only Proven,<br>Quality Products</div>
  <div class="feature" style="left:132px;top:233px"><i role="img" aria-label="Handshake icon"></i>You Can Rely<br>On Us</div>
  <div class="feature" style="left:363px;top:233px"><i role="img" aria-label="Flooring icon"></i>Experienced Flooring<br>Specialists</div>
  <div class="feature" style="left:132px;top:333px"><i role="img" aria-label="Communication icon"></i>Clear, Honest<br>Communication</div>
  <div class="feature" style="left:363px;top:333px"><i role="img" aria-label="Customer icon"></i>Customer Focused<br>Values</div>
  <div class="btn" style="left:136px;top:441px;width:208px;height:45px">Free Quotation</div>
  <div class="abs" style="left:379px;top:446px;display:flex;gap:14px;align-items:center">
    <svg width="30" height="30" viewBox="0 0 24 24" fill="none" stroke="#34509a" stroke-width="1.4"><path d="M5 3h3l2 5-2 1.5a11 11 0 0 0 6 6L15.5 14l5 2v3a2 2 0 0 1-2 2A16 16 0 0 1 3 5a2 2 0 0 1 2-2z"/></svg>
    <div style="border-left:1px solid var(--line);padding-left:14px"><div style="font-size:15px;color:var(--ink)">Call Us</div><div style="font-size:17px;font-weight:800;color:var(--blue)">+61 400 555 123</div></div>
  </div>
</section>

<section class="services">
  <h2 class="heading abs center" style="top:54px">What We Do</h2>
  <div class="rule" style="left:582px;top:118px"></div>
  <div class="arrow" style="left:61px;top:353px"><svg width="14" height="14" viewBox="0 0 14 14"><path d="M9 2 4 7l5 5" stroke="#34509a" stroke-width="1.6" fill="none"/></svg></div>
  <div class="arrow" style="left:1105px;top:353px"><svg width="14" height="14" viewBox="0 0 14 14"><path d="m5 2 5 5-5 5" stroke="#34509a" stroke-width="1.6" fill="none"/></svg></div>
  <div class="card" style="left:132px"><div class="pic" role="img" aria-label="Epoxy floor beside brick wall" style="background:linear-gradient(180deg,#8b5a4a 0%,#a89d88 40%,#c2b49a)"></div><h3>Epoxy Flooring</h3><p>Lorem ipsum dolor sit amet, consectetur adipiscing elit, sed do eiusmod tem por incididunt ut labore</p><div class="more">READ MORE</div></div>
  <div class="card active" style="left:370px"><div class="pic" role="img" aria-label="Polished concrete surface" style="background:linear-gradient(160deg,#c8b27a,#dcd6c8 60%,#b9b4a8)"></div><h3>Polished Concrete</h3><p>Lorem ipsum dolor sit amet, consectetur adipiscing elit, sed do eiusmod tem por incididunt ut labore</p><div class="more">READ MORE</div></div>
  <div class="card" style="left:606px"><div class="pic" role="img" aria-label="Sealed concrete driveway" style="background:linear-gradient(180deg,#4d5248 0%,#b9bbb8 40%,#a7a9a7)"></div><h3>Concrete Sealing</h3><p>Lorem ipsum dolor sit amet, consectetur adipiscing elit, sed do eiusmod tem por incididunt ut labore</p><div class="more">READ MORE</div></div>
  <div class="card" style="left:845px"><div class="pic" role="img" aria-label="Painted concrete step by brick wall" style="background:linear-gradient(180deg,#8d4d3e 0%,#d8cdb6 45%,#4b4b50)"></div><h3>Concrete Painting</h3><p>Lorem ipsum dolor sit amet, consectetur adipiscing elit, sed do eiusmod tem por incididunt ut labore</p><div class="more">READ MORE</div></div>
</section>

<section class="testimonials">
  <h2 class="heading abs center" style="top:57px">Testimonials</h2>
  <div class="rule" style="left:582px;top:125px"></div>
  <div class="qmark" style="left:196px;top:150px">&ldquo;</div>
  <p class="quote">Sed ut perspiciatis unde omnis iste natus error sit voluptatem accusantium doloremque laudantium, totam rem aperiam, eaque ipsa quae ab illo inventore veritatis et quasi architecto beatae vitae dicta sunt explicabo. Nemo enim ipsam voluptatem quia voluptas sit aspernatur aut odit aut fugit, sed quia consequuntur magni dolores eos qui ratione voluptatem sequi nesciunt. Neque porro quisquam est, qui dolorem ipsum quia dolor sit</p>
  <div class="qmark" style="left:890px;top:310px">&rdquo;</div>
  <div class="abs center" style="top:365px;text-align:center;font-size:13px;font-weight:800;color:var(--blue);letter-spacing:1px">MARCUS</div>
  <div class="dots" style="left:558px;top:432px"><i class="on" style="border:none"></i><i style="background:#c4c4c8"></i><i style="background:#c4c4c8"></i><i style="background:#c4c4c8"></i><i style="background:#c4c4c8"></i></div>
</section>

<section class="projects">
  <h2 class="heading abs center" style="top:50px">Our Projects</h2>
  <div class="rule" style="left:582px;top:115px"></div>
  <div class="shot" role="img" aria-label="Concrete path beside garden bed" style="left:13px;width:220px;background:linear-gradient(180deg,#d8d8d6,#7d7f7d 55%,#4e7a30)"></div>
  <div class="shot" role="img" aria-label="Exposed aggregate floor close-up" style="left:251px;width:220px;background:linear-gradient(135deg,#cfcdc8,#b5b1aa)"></div>
  <div class="shot" role="img" aria-label="Smooth grey concrete under a carport" style="left:489px;width:222px;background:linear-gradient(180deg,#6a6660,#a29e98 50%,#8d8984)"></div>
  <div class="shot" role="img" aria-label="Concrete slab beside garage" style="left:729px;width:220px;background:linear-gradient(180deg,#5d7355,#b4b4b2 45%,#9c9c9a)"></div>
  <div class="shot" role="img" aria-label="Concrete path beside brick house" style="left:969px;width:221px;background:linear-gradient(180deg,#98b0c8,#c2a884 45%,#8b8d8f)"></div>
  <svg class="abs" style="left:36px;top:3575px;top:275px" width="28" height="44" viewBox="0 0 28 44"><path d="M22 4 6 22l16 18" stroke="#fff" stroke-width="4" fill="none"/></svg>
  <svg class="abs" style="left:1140px;top:275px" width="28" height="44" viewBox="0 0 28 44"><path d="m6 4 16 18L6 40" stroke="#fff" stroke-width="4" fill="none"/></svg>
</section>

<section class="quotation" role="img" aria-label="Background photo of dark aggregate concrete">
  <div class="form-card">
    <h2 class="heading abs" style="left:0;width:702px;text-align:center;top:40px;font-size:29px">Request a Free Quotation</h2>
    <div class="field" style="left:55px;top:143px;width:291px">First Name*</div>
    <div class="field" style="left:359px;top:143px;width:291px">Last Name*</div>
    <div class="field" style="left:55px;top:204px;width:291px">Email*</div>
    <div class="field" style="left:359px;top:204px;width:291px">Phone number*</div>
    <div class="field" style="left:55px;top:264px;width:595px">Company name</div>
    <div class="field" style="left:55px;top:321px;width:595px;justify-content:space-between">What flooring service do you require?<svg width="20" height="12" viewBox="0 0 20 12"><path d="m2 2 8 8 8-8" stroke="#1f2330" stroke-width="1.6" fill="none"/></svg></div>
    <div class="field" style="left:55px;top:378px;width:595px;height:89px;align-items:flex-start;padding-top:12px">Message</div>
    <div class="btn" style="left:297px;top:497px;width:104px;height:40px">Submit</div>
  </div>
</section>

<footer class="site-footer">
  <div class="brand">StoneVista</div>
  <h4 style="left:470px">Contact Us</h4>
  <div class="foot-list" style="left:470px">
    <div style="display:flex;gap:8px"><svg width="10" height="14" viewBox="0 0 10 14"><path d="M5 0a5 5 0 0 0-5 5c0 4 5 9 5 9s5-5 5-9a5 5 0 0 0-5-5z" fill="#fff"/></svg><span>48 Harbour Row,<br>Adelaide SA 5000</span></div>
    <div style="display:flex;gap:8px;margin-top:6px"><svg width="10" height="10" viewBox="0 0 24 24"><path d="M5 3h3l2 5-2 1.5a11 11 0 0 0 6 6L15.5 14l5 2v3a2 2 0 0 1-2 2A16 16 0 0 1 3 5a2 2 0 0 1 2-2z" fill="#fff"/></svg>+61 400 555 123</div>
    <div style="display:flex;gap:8px;margin-top:6px"><svg width="11" height="9" viewBox="0 0 11 9"><rect width="11" height="9" fill="#fff"/><path d="m0 0 5.5 5L11 0" stroke="#34509a" fill="none"/></svg>info@stonevista.net</div>
  </div>
  <h4 style="left:710px">Menu</h4>
  <div class="foot-list" style="left:710px">Home<br>Residential<br>Commercial<br>About Us<br>Gallery<br>Contact Us</div>
  <h4 style="left:886px">Follow Us</h4>
  <div class="social" aria-label="Social links"><i></i><i></i><i></i><i></i><i></i></div>
  <div class="abs" style="left:132px;top:237px;width:936px;height:1px;background:rgba(255,255,255,.35)"></div>
  <div class="abs center" style="top:264px;text-align:center;font-size:12px">Copyright &copy; 2024 All Rights Reserved</div>
</footer>

</body>
</html>
```